Arbor Stone - bathroom remodel service

Want some vehicle wrap made that will pop and stand out. I like simple concepts but I’m open. I will upload photo of my logo in the files and would like something made around it. I provide tile service in contraction industry. My flagship product is bathroom remodels
Updates

Vehicle wrap is for a kelvor roamer cargo van. Medium or high roof model works just so that’s clear

Target Market(s)

Home owners

Industry/Entity Type

Construction

Requirements
Must have
• The logo colors
Nice to have
• I would like the design to be straight and not slanted
Should not have
• The name on the van should be straight please. So customers can read clearly.

```html
<!DOCTYPE html>
<html lang="en">
<head>
<meta charset="utf-8">
<title>Arbor Stone – Kelvor Roamer Van Wrap</title>
<link href="https://fonts.googleapis.com/css2?family=Montserrat:wght@700;800&family=Josefin+Sans:wght@600;700&display=swap" rel="stylesheet">
<style>
  :root {
    --navy: #0f2a5c;
    --orange: #e8650f;
    --white: #ffffff;
    --trim: #1d1d1f;
    --glass: #2a2d33;
    --tyre: #262626;
    --page: #ffffff;
  }
  html, body {
    margin: 0;
    padding: 0;
    width: 1200px;
    height: 1200px;
    overflow: hidden;
    background: var(--page);
  }
  .wrap-sheet { display: block; width: 1200px; height: 1200px; }
  .brand-name { font-family: "Montserrat", sans-serif; font-weight: 800; }
  .contact-phone { font-family: "Josefin Sans", sans-serif; font-weight: 700; }
  .contact-web { font-family: "Josefin Sans", sans-serif; font-weight: 700; fill: var(--orange); }
  .body-white { fill: var(--white); stroke: #d8d8d8; stroke-width: 1.5; }
  .body-navy { fill: var(--navy); }
  .trim { fill: var(--trim); }
  .glass { fill: var(--glass); }
  .tyre { fill: var(--tyre); }
  .hub { fill: #b9bcc0; }
  .band-white { fill: var(--white); }
  .frame-white { fill: none; stroke: var(--white); stroke-width: 9; }
  .skyline-side { fill: #c5cede; }
  .skyline-rear { fill: #2f4a80; }
  .lamp { fill: #b3141c; }
</style>
</head>
<body>
<svg class="wrap-sheet" viewBox="0 0 1200 1200" xmlns="http://www.w3.org/2000/svg">
  <defs>
    <clipPath id="side-body-clip">
      <path d="M150 410 L150 370 Q152 345 175 335 L255 312 Q280 300 300 285 L385 215 Q410 160 470 150 L1020 138 Q1040 140 1045 160 L1052 300 L1056 440 L1056 462 L150 462 Z"/>
    </clipPath>
  </defs>

  <!-- Side elevation -->
  <g class="van-side">
    <path class="body-white" d="M150 410 L150 370 Q152 345 175 335 L255 312 Q280 300 300 285 L385 215 Q410 160 470 150 L1020 138 Q1040 140 1045 160 L1052 300 L1056 440 L1056 462 L150 462 Z"/>
    <g clip-path="url(#side-body-clip)">
      <rect class="body-navy" x="733" y="130" width="330" height="340"/>
      <rect class="band-white" x="733" y="157" width="330" height="8"/>
      <rect class="trim" x="150" y="408" width="906" height="38"/>
      <rect class="band-white" x="370" y="447" width="363" height="10"/>
    </g>
    <rect class="frame-white" x="770" y="162" width="258" height="208"/>
    <text class="brand-name" x="898" y="256" fill="#ffffff" font-size="50" text-anchor="middle">Arbor</text>
    <text class="brand-name" x="898" y="316" fill="#ffffff" font-size="50" text-anchor="middle">Stone</text>

    <path class="glass" d="M270 343 L395 218 Q405 205 420 205 L475 205 L470 325 L330 340 Z"/>
    <rect class="lamp" x="1026" y="300" width="20" height="95" rx="6"/>

    <text class="brand-name" x="618" y="262" fill="#0f2a5c" font-size="24" text-anchor="middle">Arbor Stone</text>

    <rect class="skyline-side" x="436" y="296" width="296" height="112" role="img" aria-label="Line illustration of trees and town houses along a low hillside"/>

    <text class="contact-phone" x="297" y="369" fill="#0f2a5c" font-size="11">&#9990; +1 555 014-2287</text>
    <text class="contact-web" x="297" y="384" font-size="11">www.arborstone.com</text>

    <circle class="tyre" cx="297" cy="468" r="56"/>
    <circle class="hub" cx="297" cy="468" r="34"/>
    <circle class="tyre" cx="882" cy="468" r="56"/>
    <circle class="hub" cx="882" cy="468" r="34"/>
  </g>

  <!-- Front elevation -->
  <g class="van-front">
    <path class="body-white" d="M175 622 L470 622 Q485 624 490 640 L520 860 L535 960 L535 1075 L100 1075 L100 960 L115 860 L150 640 Q155 624 175 622 Z"/>
    <path class="glass" d="M155 692 L488 692 L500 832 L143 832 Z"/>
    <rect class="trim" x="68" y="788" width="44" height="72" rx="8"/>
    <rect class="trim" x="525" y="792" width="50" height="72" rx="8"/>
    <path class="trim" d="M205 912 L435 912 L445 1000 L195 1000 Z"/>
    <rect class="trim" x="98" y="1000" width="440" height="80" rx="12"/>
    <rect class="tyre" x="104" y="1080" width="58" height="45" rx="10"/>
    <rect class="tyre" x="475" y="1080" width="58" height="45" rx="10"/>
    <text class="brand-name" x="318" y="886" fill="#0f2a5c" font-size="22" text-anchor="middle">Arbor Stone</text>
  </g>

  <!-- Rear elevation -->
  <g class="van-rear">
    <path class="body-navy" d="M705 640 Q720 628 760 626 L1040 626 Q1068 628 1075 645 L1080 720 L1085 985 L678 985 L682 720 Z"/>
    <rect class="band-white" x="690" y="655" width="390" height="10"/>
    <rect class="band-white" x="683" y="948" width="400" height="10"/>
    <rect class="lamp" x="813" y="624" width="150" height="12" rx="5"/>
    <rect class="lamp" x="678" y="850" width="20" height="120" rx="6"/>
    <rect class="lamp" x="1064" y="850" width="20" height="120" rx="6"/>
    <line x1="882" y1="640" x2="882" y2="985" stroke="#0a1f48" stroke-width="2"/>

    <text class="brand-name" x="881" y="792" fill="#ffffff" font-size="36" text-anchor="middle">Arbor Stone</text>

    <text class="contact-phone" x="742" y="895" fill="#ffffff" font-size="13">&#9990; +1 555 014-2287</text>
    <text class="contact-web" x="742" y="912" font-size="13">www.arborstone.com</text>

    <rect class="skyline-rear" x="880" y="866" width="182" height="80" role="img" aria-label="Line illustration of trees and town houses along a low hillside"/>

    <rect class="trim" x="676" y="985" width="412" height="70" rx="10"/>
    <rect class="tyre" x="692" y="1055" width="55" height="70" rx="10"/>
    <rect class="tyre" x="1018" y="1055" width="55" height="70" rx="10"/>
  </g>
</svg>
</body>
</html>
```